Willow Current Mind Studio

I need a brain fitness website that is on the WordPress platform. It needs to feel friendly and relaxing. We are not a physical health gym, but a brain health coaching facility. I can produce hundreds of professional photos. It can be one long page or five short pages.

Industry/Entity Type

Health And Wellness

```html
<!DOCTYPE html>
<html lang="en">
<head>
<meta charset="utf-8">
<title>Willow Current Mind Studio</title>
<link href="https://fonts.googleapis.com/css2?family=Raleway:wght@400;500;600&family=Open+Sans:wght@400&display=swap" rel="stylesheet">
<style>
:root{
  --bg:#878787;
  --paper:#ffffff;
  --teal:#1c6a86;
  --teal-dark:#135a75;
  --magenta:#a3195b;
  --sky:#2fa6d9;
  --field:#efefef;
  --ink:#2f2f2f;
  --panel:rgba(40,40,42,.78);
  --footer:#3a3a3a;
}
*{margin:0;padding:0;box-sizing:border-box}
html,body{width:1200px;height:1200px;overflow:hidden;background:var(--bg)}
body{position:relative;font-family:"Raleway",sans-serif;color:var(--teal)}
.sheet{position:absolute;background:var(--paper);overflow:hidden}
.sheet--top{left:55px;top:41px;width:668px;height:890px;z-index:2}
.sheet--bottom{left:503px;top:544px;width:640px;height:604px;z-index:1}
.abs{position:absolute}

/* header */
.brand{left:30px;top:14px;width:150px;text-align:center}
.brand__dot{display:block;width:36px;height:36px;margin:0 auto 6px;border-radius:50%;background:var(--teal);opacity:.85}
.brand__name{font-size:12px;font-weight:600;color:var(--magenta);letter-spacing:.3px;line-height:1.15}
.nav{top:57px;left:213px;display:flex;gap:12px;font-size:8.5px;font-weight:600;color:var(--teal)}
.nav a:first-child{color:var(--magenta)}
.nav a{text-decoration:none;color:inherit}
.signin{top:57px;left:558px;font-size:7.5px;font-weight:600;color:var(--magenta)}

/* hero */
.hero{left:0;top:104px;width:668px;height:261px;background:linear-gradient(90deg,#d9a9c6 0%,#b9cfd9 40%,#a9d2e0 70%,#9dc7c8 100%)}
.hero__ground{left:0;top:150px;width:668px;height:111px;background:linear-gradient(180deg,rgba(180,200,150,0) 0%,rgba(196,200,120,.7) 100%)}
.hero__text{left:84px;top:93px;width:500px;text-align:center;font-size:10px;line-height:1.3;color:var(--magenta);font-weight:500}
.btn{display:flex;align-items:center;justify-content:center;font-weight:500;color:#fff}
.hero__btn{left:294px;top:138px;width:80px;height:19px;background:var(--teal-dark);font-size:8px}

/* about */
.h2{font-size:16px;font-weight:500;color:var(--teal);text-align:center}
.about__title{left:0;width:668px;top:397px}
.welcome{left:34px;top:484px;width:240px;text-align:center}
.welcome__title{font-size:10px;font-weight:600;color:var(--teal)}
.welcome__title span{color:var(--magenta)}
.welcome__sub{font-size:9.5px;color:var(--teal);margin-top:3px}
.welcome__body{font-family:"Open Sans",sans-serif;font-size:7.6px;line-height:1.6;color:var(--teal);margin-top:14px}
.about__btn{left:127px;top:587px;width:55px;height:18px;background:var(--magenta);font-size:9.5px}
.photo{border:3px solid #fff;box-shadow:0 1px 3px rgba(0,0,0,.25)}
.photo--class{left:369px;top:439px;width:156px;height:107px;background:linear-gradient(135deg,#f0e4d8,#d8c9c0 60%,#8ec6d4)}
.photo--screen{left:470px;top:525px;width:157px;height:106px;background:linear-gradient(90deg,#0d1320 0%,#151c2c 55%,#e9eef2 80%)}

/* services */
.services__title{left:0;width:668px;top:658px}
.services{left:0;top:695px;width:668px;height:195px;background:linear-gradient(90deg,#e6e3e0 0%,#cfc9c4 40%,#6a4a40 60%,#3b3b3e 100%)}
.services__panel{left:334px;top:0;width:334px;height:195px;background:var(--panel)}
.service{left:36px;display:flex;align-items:center;gap:11px;font-family:"Open Sans",sans-serif;font-size:7.6px;color:#fff}
.service svg{width:20px;height:20px;flex:none}

/* newsletter */
.news{left:0;top:0;width:640px;height:132px;background:linear-gradient(90deg,#1e76a4 0%,#2ea7dc 50%,#2aa0d2 70%,#166c8d 100%)}
.news__title{left:220px;top:24px;font-size:14px;font-weight:600;color:#fff}
.news__title span{color:var(--magenta)}
.news__input{left:220px;top:64px;width:181px;height:29px;background:var(--field);font-size:7px;color:#888;display:flex;align-items:center;justify-content:center}
.news__btn{left:401px;top:64px;width:54px;height:29px;background:var(--magenta);font-size:7px}

/* gallery */
.gallery__title{left:286px;top:150px;font-size:15px}
.tile{width:157px;height:110px;border:3px solid #fff;box-shadow:0 1px 3px rgba(0,0,0,.25)}
.tile--a{left:73px;top:204px;background:#e2dfd9}
.tile--b{left:242px;top:204px;background:linear-gradient(135deg,#f6f6f6,#c9c9cc 50%,#f2f2f2)}
.tile--c{left:410px;top:204px;background:linear-gradient(180deg,#6d7268 0%,#9da094 55%,#d2d4cc 100%)}
.tile--d{left:73px;top:328px;background:linear-gradient(180deg,#f4f4f4 60%,#d96b4e 100%)}
.tile--e{left:242px;top:328px;background:linear-gradient(180deg,#9fb6c4 0%,#4ba9d6 50%,#c9a7c3 100%)}
.tile--f{left:410px;top:328px;background:linear-gradient(180deg,#d9cfc3 0%,#b9a89a 55%,#5a3b45 80%,#d6c2a4 100%)}

/* contacts */
.contacts__title{left:42px;top:475px;font-size:15px}
.contacts__list{left:42px;top:502px;font-size:9px;line-height:17px;color:var(--magenta)}
.field{background:var(--field);font-size:7px;color:var(--magenta);padding:5px 7px}
.field--email{left:272px;top:477px;width:178px;height:18px;padding-top:4px}
.field--msg{left:272px;top:503px;width:178px;height:39px}
.send{left:459px;top:477px;width:54px;height:18px;background:var(--field);font-size:7px;color:var(--magenta);font-weight:500}
.socials{left:463px;top:521px;display:flex;gap:5px}
.socials span{width:10px;height:10px;border-radius:50%;background:var(--magenta)}
.socials span:nth-child(odd){background:var(--teal)}
.footer{left:0;top:574px;width:640px;height:30px;background:var(--footer)}
.footer__text{left:72px;top:10px;font-size:7.5px;color:#e8e8e8}
</style>
</head>
<body>

<section class="sheet sheet--bottom">
  <div class="abs news"></div>
  <h2 class="abs news__title">JOIN TO OUR <span>NEWSLETTER</span></h2>
  <div class="abs news__input">EXAMPLE@MAIL.COM</div>
  <div class="abs btn news__btn">JOIN</div>

  <h2 class="abs h2 gallery__title">GALLERY</h2>
  <div class="abs tile tile--a" role="img" aria-label="Photo of a woman in a yoga pose"></div>
  <div class="abs tile tile--b" role="img" aria-label="Photo of a man stretching over an exercise ball"></div>
  <div class="abs tile tile--c" role="img" aria-label="Photo of a group doing yoga outdoors by a rock cliff"></div>
  <div class="abs tile tile--d" role="img" aria-label="Photo of a person balancing in a stretch"></div>
  <div class="abs tile tile--e" role="img" aria-label="Photo of a group meditating on mats outdoors"></div>
  <div class="abs tile tile--f" role="img" aria-label="Photo of a woman stretching on a mat beside candles"></div>

  <h2 class="abs h2 contacts__title">CONTACTS</h2>
  <div class="abs contacts__list">
    <div>+012 1457 574</div>
    <div>WWW.EXAMPLE.COM</div>
    <div>1204 ,EXAMPLE,2104</div>
  </div>
  <div class="abs field field--email">EMAIL :</div>
  <div class="abs btn send">SEND</div>
  <div class="abs field field--msg">MESSAGE :</div>
  <div class="abs socials"><span></span><span></span><span></span><span></span></div>

  <footer class="abs footer"><div class="abs footer__text">ALL COPYRIGHTS RESERVED</div></footer>
</section>

<section class="sheet sheet--top">
  <header>
    <div class="abs brand">
      <span class="brand__dot"></span>
      <div class="brand__name">WILLOW CURRENT<br>MIND STUDIO</div>
    </div>
    <nav class="abs nav">
      <a>HOME</a><a>ABOUT</a><a>SERVICES</a><a>NEWSLETTER</a><a>GALLERY</a><a>CONTACTS</a>
    </nav>
    <div class="abs signin">SIGN IN / SIGN UP</div>
  </header>

  <div class="abs hero" role="img" aria-label="Photo of a woman with open arms in a meadow facing misty hills">
    <div class="abs hero__ground"></div>
    <p class="abs hero__text">Lorem ipsum dolor sit amet, consectetur adipiscing elit, sed do eiusmod tempor incididunt ut labore et<br>dolore magna aliqua. Ut enim ad minim veniam,<br>quis nostrud exercitation</p>
    <div class="abs btn hero__btn">VEIW MORE</div>
  </div>

  <h2 class="abs h2 about__title">ABOUT</h2>
  <div class="abs welcome">
    <div class="welcome__title">WELCOME TO <span>WILLOW CURRENT</span></div>
    <div class="welcome__sub">MIND STUDIO</div>
    <p class="welcome__body">Lorem ipsum dolor sit amet, consectetur adipiscing elit,<br>sed do eiusmod tempor incididunt ut labore et dolore ma<br>gna aliqua. Ut enim ad minim veniam, quis nostrud<br>exercitation ullamco laboris nisi ut aliquip</p>
  </div>
  <div class="abs btn about__btn">MORE</div>
  <div class="abs photo photo--class" role="img" aria-label="Photo of children stretching on mats in a class"></div>
  <div class="abs photo photo--screen" role="img" aria-label="Photo of a girl touching a light reaction training wall"></div>

  <h2 class="abs h2 services__title">SERVICES</h2>
  <div class="abs services" role="img" aria-label="Photo of a woman in a seated forward fold">
    <div class="abs services__panel">
      <div class="abs service" style="top:23px"><svg viewBox="0 0 20 20"><polygon points="5,2 15,2 19,10 15,18 5,18 1,10" fill="none" stroke="#a3195b" stroke-width="2"/></svg>Lorem ipsum dolor sit amet, consectetur adipiscing elit</div>
      <div class="abs service" style="top:66px"><svg viewBox="0 0 20 20"><polygon points="5,2 15,2 19,10 15,18 5,18 1,10" fill="none" stroke="#a3195b" stroke-width="2"/></svg>Lorem ipsum dolor sit amet, consectetur adipiscing elit</div>
      <div class="abs service" style="top:109px"><svg viewBox="0 0 20 20"><polygon points="5,2 15,2 19,10 15,18 5,18 1,10" fill="none" stroke="#a3195b" stroke-width="2"/></svg>Lorem ipsum dolor sit amet, consectetur adipiscing elit</div>
      <div class="abs service" style="top:153px"><svg viewBox="0 0 20 20"><polygon points="5,2 15,2 19,10 15,18 5,18 1,10" fill="none" stroke="#a3195b" stroke-width="2"/></svg>Lorem ipsum dolor sit amet, consectetur adipiscing elit</div>
    </div>
  </div>
</section>

</body>
</html>
```